Visual consulting framework

Tamsworth Advisory is a financial consulting business that takes it clients on the following journey:
1. Get fit (disciplined)
2. Get funded (access to capital)
3. Get big (grow)
4. Get out (exit with wealth)
Over thirty years we have identified that the key to being successful on this journey are the following elements or components.
1. Vision
2. Strategy
3. Structure
4. Product & services
5. Sales and marketing
6. System and processes
7. People
8. Culture
9. Finance
10. M&A
11. Performance monitoring
12. Risk management
We require a visual representation of these elements and the journey to communicate to clients and prospects in marketing material.

```html
<!DOCTYPE html>
<html lang="en">
<head>
<meta charset="utf-8">
<title>Tamsworth Advisory – Consulting Framework</title>
<link rel="stylesheet" href="https://fonts.googleapis.com/css2?family=Montserrat:wght@400;500;600&display=swap">
<style>
  :root {
    --navy: #13294b;
    --white: #ffffff;
    --paper: #f4f4f4;
    --orange: #f7931e;
    --sky: #29a8e0;
  }
  html, body {
    margin: 0;
    width: 675px;
    height: 1200px;
    overflow: hidden;
    background: #000;
  }
  .canvas {
    position: relative;
    width: 675px;
    height: 1200px;
    font-family: "Montserrat", Arial, sans-serif;
  }
  .panel {
    position: absolute;
    left: 60.6px;
    width: 553.75px;
    height: 311.25px;
    display: block;
  }
  .panel--ocean { top: 67.5px; }
  .panel--mist  { top: 444.4px; }
  .panel--ember { top: 821.25px; }

  /* Variant: ocean blue on orange */
  .panel--ocean {
    --band-bottom: var(--orange);
    --headline: var(--navy);
    --brand: var(--orange);
    --label-top: var(--navy);
    --axis: var(--navy);
    --end-lt: #35b1e0; --end-lb: #35b1e0; --end-rt: #35b1e0; --end-rb: #35b1e0;
    --t1: #35b1e0; --t2: #35b1e0; --t3: #35b1e0; --t4: #35b1e0;
    --b1: #35b1e0; --b2: #35b1e0; --b3: #35b1e0; --b4: #35b1e0;
    --inner-l: #6fc6ea; --inner-r: #b8ad98;
    --s1: #6fc6ea; --s2: #b8ad98; --s3: #112a4a; --s4: #b8ad98;
    --st1: var(--navy); --st2: var(--navy); --st3: var(--white); --st4: var(--navy);
    --pill: #13294b;
    --icon: var(--white);
  }
  /* Variant: soft blue tints */
  .panel--mist {
    --band-bottom: var(--orange);
    --headline: #2a86c8;
    --brand: var(--orange);
    --label-top: var(--navy);
    --axis: var(--navy);
    --end-lt: #e3f1f9; --end-lb: #6fb0e0; --end-rt: #e3f1f9; --end-rb: #e3f1f9;
    --t1: #8ccbe9; --t2: #a9d8ee; --t3: #cfe8f4; --t4: #bfe1f1;
    --b1: #d6ecf6; --b2: #a9d8ee; --b3: #cfe8f4; --b4: #d6ecf6;
    --inner-l: #4ba5d9; --inner-r: #4ba5d9;
    --s1: #4ba5d9; --s2: #4ba5d9; --s3: #4ba5d9; --s4: #4ba5d9;
    --st1: var(--white); --st2: var(--white); --st3: var(--white); --st4: var(--white);
    --pill: #3c4a78;
    --icon: var(--navy);
  }
  /* Variant: warm reds on blue */
  .panel--ember {
    --band-bottom: var(--sky);
    --headline: var(--navy);
    --brand: var(--orange);
    --label-top: #8a8a8a;
    --axis: #6b1f1a;
    --end-lt: #f5a05a; --end-lb: #e06a2a; --end-rt: #e0506a; --end-rb: #e8788a;
    --t1: #e03a2e; --t2: #e8584a; --t3: #ef8a7c; --t4: #5a1f1e;
    --b1: #b0433a; --b2: #fdd36a; --b3: #8a3530; --b4: #f9b122;
    --inner-l: #ffffff; --inner-r: #35a8e0;
    --s1: #ffffff; --s2: #e0d8c4; --s3: #c2b8a3; --s4: #35a8e0;
    --st1: var(--navy); --st2: var(--navy); --st3: var(--navy); --st4: var(--white);
    --pill: #13294b;
    --icon: var(--white);
  }
  .sprite { position: absolute; width: 0; height: 0; overflow: hidden; }
</style>
</head>
<body>
<main class="canvas">
  <svg class="sprite" aria-hidden="true">
    <symbol id="framework" viewBox="0 0 886 498">
      <!-- background bands -->
      <rect class="band-top" x="0" y="0" width="886" height="299" style="fill:var(--paper)"/>
      <rect class="band-bottom" x="0" y="299" width="886" height="199" style="fill:var(--band-bottom)"/>

      <!-- brand -->
      <circle class="brand-mark" cx="72" cy="52" r="26" style="fill:var(--brand)"/>
      <text class="brand-name" x="118" y="50" font-family="Montserrat, Arial, sans-serif" font-size="19" font-weight="400" style="fill:var(--brand)"><tspan x="118">Tamsworth</tspan><tspan x="118" dy="22">Advisory</tspan></text>
      <line class="brand-divider" x1="251" y1="26" x2="251" y2="86" stroke="#9aa3ad" stroke-width="1.5"/>
      <text class="headline" text-anchor="middle" font-family="Montserrat, Arial, sans-serif" font-size="26.5" font-weight="500" style="fill:var(--headline)"><tspan x="572" y="49">Our purpose is clear, we get companies</tspan><tspan x="572" y="80">and their founders, fit, funded, big and out</tspan></text>

      <!-- outer ring ends -->
      <path class="ring-end" d="M217.5 155 A143.5 143.5 0 0 0 74 298.5 L443 298.5 L443 155 Z" style="fill:var(--end-lt)"/>
      <path class="ring-end" d="M74 298.5 A143.5 143.5 0 0 0 217.5 442 L443 442 L443 298.5 Z" style="fill:var(--end-lb)"/>
      <path class="ring-end" d="M668.5 155 A143.5 143.5 0 0 1 812 298.5 L443 298.5 L443 155 Z" style="fill:var(--end-rt)"/>
      <path class="ring-end" d="M812 298.5 A143.5 143.5 0 0 1 668.5 442 L443 442 L443 298.5 Z" style="fill:var(--end-rb)"/>

      <!-- element cells -->
      <rect class="cell" x="188" y="155" width="127.5" height="70" style="fill:var(--t1)"/>
      <rect class="cell" x="315.5" y="155" width="127.5" height="70" style="fill:var(--t2)"/>
      <rect class="cell" x="443" y="155" width="127.5" height="70" style="fill:var(--t3)"/>
      <rect class="cell" x="570.5" y="155" width="126.5" height="70" style="fill:var(--t4)"/>
      <rect class="cell" x="188" y="374" width="127.5" height="68" style="fill:var(--b1)"/>
      <rect class="cell" x="315.5" y="374" width="127.5" height="68" style="fill:var(--b2)"/>
      <rect class="cell" x="443" y="374" width="127.5" height="68" style="fill:var(--b3)"/>
      <rect class="cell" x="570.5" y="374" width="126.5" height="68" style="fill:var(--b4)"/>

      <!-- journey track -->
      <path class="track-end" d="M443 224 L218.5 224 A75.5 75.5 0 0 0 218.5 375 L443 375 Z" style="fill:var(--inner-l)"/>
      <path class="track-end" d="M443 224 L667.5 224 A75.5 75.5 0 0 1 667.5 375 L443 375 Z" style="fill:var(--inner-r)"/>
      <rect class="stage" x="188" y="224" width="127.5" height="151" style="fill:var(--s1)"/>
      <rect class="stage" x="315.5" y="224" width="127.5" height="151" style="fill:var(--s2)"/>
      <rect class="stage" x="443" y="224" width="127.5" height="151" style="fill:var(--s3)"/>
      <rect class="stage" x="570.5" y="224" width="126.5" height="151" style="fill:var(--s4)"/>

      <!-- axes -->
      <g class="axes" style="stroke:var(--axis)" stroke-width="1.3">
        <line x1="36" y1="299" x2="850" y2="299"/>
        <line x1="188" y1="112" x2="188" y2="478"/>
        <line x1="315.5" y1="112" x2="315.5" y2="478"/>
        <line x1="443" y1="112" x2="443" y2="478"/>
        <line x1="570.5" y1="112" x2="570.5" y2="478"/>
        <line x1="697" y1="112" x2="697" y2="478"/>
      </g>
      <g class="axis-heads" style="fill:var(--axis)">
        <polygon points="32,299 40,296 40,302"/>
        <polygon points="854,299 846,296 846,302"/>
        <polygon points="188,108 185,115 191,115"/><polygon points="188,482 185,475 191,475"/>
        <polygon points="315.5,108 312.5,115 318.5,115"/><polygon points="315.5,482 312.5,475 318.5,475"/>
        <polygon points="443,108 440,115 446,115"/><polygon points="443,482 440,475 446,475"/>
        <polygon points="570.5,108 567.5,115 573.5,115"/><polygon points="570.5,482 567.5,475 573.5,475"/>
        <polygon points="697,108 694,115 700,115"/><polygon points="697,482 694,475 700,475"/>
      </g>

      <!-- market leader -->
      <rect class="goal" x="189" y="270" width="508" height="56" rx="28" style="fill:var(--pill)"/>
      <text class="goal-text" x="443" y="311" text-anchor="middle" font-family="Montserrat, Arial, sans-serif" font-size="32" font-weight="500" letter-spacing="8" fill="#fff">MARKET LEADER</text>

      <!-- journey stages -->
      <g class="stage-text" font-family="Montserrat, Arial, sans-serif" font-size="12.5" font-weight="500" text-anchor="middle">
        <text x="251.5" y="252" style="fill:var(--st1)">— Get Fit →</text>
        <text x="379" y="253" style="fill:var(--st2)">— Get Funded →</text>
        <text x="506.5" y="253" style="fill:var(--st3)">— Get Big →</text>
        <text x="633.5" y="253" style="fill:var(--st4)">Get Out</text>
        <text x="251.5" y="354" style="fill:var(--st1)">— Disciplined →</text>
        <text x="379" y="347" style="fill:var(--st2)"><tspan x="374">Access to</tspan><tspan x="374" dy="15">Capital</tspan></text>
        <text x="418" y="355" style="fill:var(--st2)">→</text>
        <text x="506.5" y="354" style="fill:var(--st3)">— Grow →</text>
        <text x="633.5" y="347" style="fill:var(--st4)"><tspan x="633.5">Exit with</tspan><tspan x="633.5" dy="15">Wealth</tspan></text>
      </g>

      <!-- element labels -->
      <g class="element-label" font-family="Montserrat, Arial, sans-serif" font-size="12.5" font-weight="500" text-anchor="middle">
        <g style="fill:var(--label-top)">
          <text x="251.5" y="136">Vision</text>
          <text x="379" y="136">Strategy</text>
          <text x="506.5" y="136">Structure</text>
          <text x="633.5" y="128">Products &amp;</text>
          <text x="633.5" y="143">Services</text>
          <text x="58" y="192">Performance</text>
          <text x="58" y="207">Monitoring</text>
          <text x="817" y="200">People</text>
        </g>
        <g fill="#fff">
          <text x="251.5" y="459">Systems</text>
          <text x="251.5" y="474">&amp; Process</text>
          <text x="379" y="467">Finance</text>
          <text x="506.5" y="459">Sales &amp;</text>
          <text x="506.5" y="474">Marketing</text>
          <text x="633.5" y="467">M&amp;A</text>
          <text x="58" y="402">Risk</text>
          <text x="58" y="417">Management</text>
          <text x="818" y="410">Culture</text>
        </g>
      </g>

      <!-- icons -->
      <g class="icons" style="fill:var(--icon);stroke:var(--icon)">
        <!-- vision: eye -->
        <g class="icon-eye" stroke="none">
          <path d="M222 189 Q251 162 280 189 Q251 216 222 189 Z"/>
          <ellipse cx="251" cy="189" rx="13" ry="13" style="fill:var(--t1)"/>
          <circle cx="251" cy="189" r="8"/>
        </g>
        <!-- strategy: pawn -->
        <g class="icon-pawn" stroke="none">
          <circle cx="379" cy="172" r="5.5"/>
          <path d="M374 179 H384 L386 199 H372 Z"/>
          <rect x="368" y="199" width="22" height="6" rx="1.5"/>
        </g>
        <!-- structure: circuit -->
        <g class="icon-circuit" fill="none" stroke-width="2.2">
          <path d="M488 176 H505 V200 M505 188 H524 M496 202 L505 194 M514 176 V188 L520 196"/>
          <circle cx="486" cy="176" r="3"/><circle cx="494" cy="204" r="3"/><circle cx="526" cy="188" r="3"/><circle cx="521" cy="198" r="3"/>
        </g>
        <!-- products & services: conveyor -->
        <g class="icon-conveyor">
          <g stroke="none">
            <rect x="612" y="170" width="10" height="10"/><rect x="628" y="170" width="10" height="10"/><rect x="644" y="170" width="10" height="10"/>
          </g>
          <rect x="609" y="186" width="48" height="13" rx="6.5" fill="none" stroke-width="2.4"/>
          <g stroke="none"><circle cx="619" cy="192.5" r="2.5"/><circle cx="633" cy="192.5" r="2.5"/><circle cx="647" cy="192.5" r="2.5"/></g>
        </g>
        <!-- systems & process: checklist -->
        <g class="icon-checklist" stroke="none">
          <rect x="228" y="398" width="5" height="3.5"/><rect x="236" y="398" width="10" height="3.5"/>
          <rect x="228" y="405" width="5" height="3.5"/><rect x="236" y="405" width="10" height="3.5"/>
          <rect x="228" y="412" width="5" height="3.5"/><rect x="236" y="412" width="10" height="3.5"/>
          <path d="M247 398 H254 L260 410 L268 398 H275 L262 418 H258 Z"/>
        </g>
        <!-- finance: coins -->
        <g class="icon-coins" stroke="none">
          <ellipse cx="385" cy="397" rx="12" ry="4"/>
          <rect x="373" y="397" width="24" height="16"/>
          <ellipse cx="385" cy="413" rx="12" ry="4"/>
          <path d="M356 408 L376 402 L380 418 L360 424 Z"/>
        </g>
        <g class="icon-coins-lines" style="stroke:var(--b2)" stroke-width="1.2" fill="none">
          <path d="M373 402 Q385 406 397 402 M373 407 Q385 411 397 407"/>
        </g>
        <!-- sales & marketing: trophy -->
        <g class="icon-trophy">
          <path d="M494 391 H519 V398 Q519 410 506.5 412 Q494 410 494 398 Z" stroke="none"/>
          <path d="M494 394 H488 Q488 404 496 404 M519 394 H525 Q525 404 517 404" fill="none" stroke-width="2.2"/>
          <rect x="504" y="412" width="5" height="6" stroke="none"/>
          <rect x="498" y="418" width="17" height="5" stroke="none"/>
        </g>
        <!-- m&a: handshake -->
        <g class="icon-handshake" stroke="none">
          <path d="M604 396 L616 392 L618 414 L606 418 Z"/>
          <path d="M663 396 L651 392 L649 414 L661 418 Z"/>
          <path d="M618 398 Q626 394 634 397 L642 394 Q648 396 649 400 L648 410 Q640 418 630 418 Q622 414 619 410 Z"/>
        </g>
        <!-- performance monitoring: clipboard -->
        <g class="icon-clipboard" fill="none" stroke-width="2.4">
          <rect x="112" y="194" width="28" height="34" rx="2"/>
          <rect x="120" y="190" width="12" height="6" stroke="none" style="fill:var(--icon)"/>
          <path d="M118 206 L122 210 L129 202 M118 219 L122 223 L129 215"/>
        </g>
        <!-- risk management: warning -->
        <g class="icon-warning">
          <path d="M130 343 L150 376 H110 Z" fill="none" stroke-width="3" stroke-linejoin="round"/>
          <rect x="128.5" y="354" width="3" height="12" stroke="none"/>
          <circle cx="130" cy="370" r="1.8" stroke="none"/>
        </g>
        <!-- people: team -->
        <g class="icon-team" stroke="none">
          <circle cx="762" cy="232" r="5"/><circle cx="750" cy="238" r="4"/><circle cx="774" cy="238" r="4"/>
          <path d="M755 242 H769 L768 262 H756 Z"/>
          <path d="M744 244 H754 V258 H746 Z"/><path d="M770 244 H780 L778 258 H770 Z"/>
        </g>
        <!-- culture: heart in hands -->
        <g class="icon-care">
          <path d="M760 362 Q752 352 745 358 Q740 364 748 370 L760 380 L772 370 Q780 364 775 358 Q768 352 760 362 Z" stroke="none"/>
          <path d="M740 366 Q738 380 752 388 M780 366 Q782 380 768 388" fill="none" stroke-width="3.2" stroke-linecap="round"/>
        </g>
      </g>
    </symbol>
  </svg>

  <svg class="panel panel--ocean" viewBox="0 0 886 498" role="img" aria-label="Tamsworth Advisory framework, blue ring on orange">
    <use href="#framework"/>
  </svg>
  <svg class="panel panel--mist" viewBox="0 0 886 498" role="img" aria-label="Tamsworth Advisory framework, soft blue tints">
    <use href="#framework"/>
  </svg>
  <svg class="panel panel--ember" viewBox="0 0 886 498" role="img" aria-label="Tamsworth Advisory framework, warm reds on blue">
    <use href="#framework"/>
  </svg>
</main>
</body>
</html>
```